Complete Website Redesign

We need a complete revamp of our website. Need to add interactive custmer catalog seection tools. Need to add customer spec input for recommended product search results. Need a cutomer lead and opportunity contact capability. Need a complete Branding message revamp. Primary visuals will be prodcut pictures and case studies.
Target Market(s)
Industrial Customers in the high durability Air movement and fan/blower space; high durability enclosure and flow industries ie. mining, chamicals, manufacturing, water treatment, chemical in use manufacturing
Look and feel

```html
<!DOCTYPE html>
<html lang="en">
<head>
<meta charset="utf-8">
<title>Duraflow Composites – Home</title>
<link href="https://fonts.googleapis.com/css2?family=PT+Sans:wght@400;700&display=swap" rel="stylesheet">
<style>
:root{
  --page:#211e1f;
  --panel:#2d2729;
  --panel-dark:#1c1a1b;
  --blue:#3f7bbd;
  --blue-dark:#2f65a6;
  --navy:#1d3f8a;
  --yellow:#ffe62e;
  --red:#8e0d0d;
  --white:#ffffff;
  --grey:#d6d6d6;
  --text:#222;
  --muted:#9a9a9a;
}
*{margin:0;padding:0;box-sizing:border-box}
html,body{width:1200px;height:972px;overflow:hidden}
body{background:var(--page);font-family:"PT Sans",Arial,sans-serif;color:var(--text);position:relative}
.top-strip{position:absolute;left:0;top:0;width:1200px;height:36px;background:#1a1718}
.site{position:absolute;left:63px;top:0;width:1081px;height:930px;background:#fff}
.topbar{position:absolute;left:0;top:0;width:100%;height:41px;background:linear-gradient(#4a88cc,#3b76b9);color:#fff;font-size:20px;letter-spacing:.5px}
.topbar .call{position:absolute;left:66px;top:8px}
.topbar .call b{color:var(--yellow);font-weight:400}
.topbar .account{position:absolute;right:74px;top:10px;font-size:17px;word-spacing:4px}
.header{position:absolute;top:41px;left:0;width:100%;height:90px;background:linear-gradient(#fff,#ececec);box-shadow:0 2px 4px rgba(0,0,0,.15)}
.brand{position:absolute;left:65px;top:16px;display:flex;align-items:center;gap:10px;color:var(--navy)}
.brand .mark{width:30px;height:30px;background:var(--navy)}
.brand .name{font-size:18px;font-weight:700;line-height:1.1}
.nav{position:absolute;left:324px;top:35px;display:flex;gap:0;font-size:16px}
.nav a{color:#222;text-decoration:none;padding:3px 17px;border-radius:6px;position:relative}
.nav a.active{background:#221f21;color:#fff}
.nav a.drop::after{content:"";position:absolute;left:50%;bottom:-9px;margin-left:-5px;border:5px solid transparent;border-top:6px solid var(--red)}
.slider{position:absolute;left:64px;top:145px;width:939px;height:304px;border:1px solid #ccc;overflow:hidden;background:#fff}
.slider svg.bg{position:absolute;left:0;top:0}
.slide-photo{position:absolute;left:150px;top:12px;width:220px;height:232px;border-radius:50% 50% 10px 10px;background:radial-gradient(circle at 50% 45%,#9aa1ad,#5f6672 70%)}
.arrow{position:absolute;top:118px}
.arrow.prev{left:30px}.arrow.next{left:468px}
.slide-copy{position:absolute;left:545px;top:108px;width:390px;text-align:center;color:#fff;font-size:21px;line-height:1.2}
.slide-copy.reflect{top:222px;transform:scaleY(-1);opacity:.18;height:60px;overflow:hidden}
.caption{position:absolute;left:33px;top:272px;font-size:22px;color:var(--navy)}
.dots{position:absolute;left:291px;top:279px;display:flex;gap:11px}
.dots i{width:15px;height:15px;border-radius:50%;background:#fff}
.dots i.on{background:#232023}
.selection{position:absolute;left:64px;top:449px;width:939px;height:88px;background:var(--panel)}
.selection h2{position:absolute;left:67px;top:28px;font-weight:400;font-size:20px;color:#fff}
.selection .field{position:absolute;left:290px;top:22px;width:425px;height:30px;background:#151214;border:1px solid #777}
.selection .btn{position:absolute;left:732px;top:22px;width:95px;height:29px;border-radius:6px;background:linear-gradient(#9cb3ae,#7d9792);color:#fff;font-size:16px;text-align:center;line-height:28px}
.selection p{position:absolute;left:0;width:100%;top:63px;text-align:center;color:#f4c21e;font-size:12px;font-weight:700}
.products{position:absolute;left:57px;top:557px;display:flex;gap:4px}
.card{position:relative;width:190px;height:213px}
.card .frame{position:absolute;left:10px;top:0;width:166px;height:213px;border:7px solid var(--grey);border-top-width:4px}
.card h3{position:absolute;left:0;top:5px;width:190px;height:30px;background:linear-gradient(#4c8ad0,#3a73b5);color:#fff;font-weight:400;font-size:14.5px;text-align:center;line-height:30px;white-space:nowrap}
.card .photo{position:absolute;left:28px;top:45px;width:134px;height:140px;border-radius:10px;background:radial-gradient(circle,#b9bec6,#8a909a 75%,#fff 76%)}
.card .more{position:absolute;right:14px;bottom:0;width:80px;height:21px;background:var(--red);color:#fff;font-size:12.5px;line-height:21px;text-align:right;padding-right:8px;clip-path:polygon(22% 0,100% 0,100% 100%,0 100%)}
.footer{position:absolute;left:0;top:791px;width:100%;height:139px;background:var(--panel)}
.footer h4{position:absolute;top:9px;color:#fff;font-size:14px;font-weight:700}
.bubble{position:absolute;left:22px;top:32px;width:195px;height:80px;background:var(--panel-dark);border-radius:12px;color:#fff;font-size:10.5px;font-weight:700;line-height:1.2;padding:9px 10px;text-align:justify}
.bubble b{color:#e02020}
.bubble-tail{position:absolute;left:105px;top:110px}
.author{position:absolute;left:158px;top:121px;color:#ccc;font-size:12px}
.social{position:absolute;left:289px;top:38px;display:grid;grid-template-columns:repeat(4,32px);gap:11px 5px}
.social i{width:31px;height:31px;border-radius:6px;background:#5c5658}
.form-box{position:absolute;top:32px;width:236px;height:110px;background:var(--panel-dark);border-radius:10px}
.form-box .in{position:absolute;left:23px;width:194px;height:20px;background:#3a3638;color:#aaa;font-size:12px;padding:2px 8px}
.fbtn{position:absolute;height:17px;color:#fff;font-size:12px;font-weight:700;text-align:center;line-height:17px}
.copyright{position:absolute;left:0;top:942px;width:1200px;text-align:center;color:var(--muted);font-size:14px}
</style>
</head>
<body>
<div class="top-strip"></div>
<div class="site">
  <div class="topbar">
    <div class="call"><b>CALL US</b> : +1 (800) 555 0142</div>
    <div class="account">LOGIN &nbsp;|&nbsp; SIGNUP</div>
  </div>
  <header class="header">
    <div class="brand"><span class="mark"></span><span class="name">DFC<br>Duraflow Composites, LLC</span></div>
    <nav class="nav">
      <a class="active">HOME</a><a class="drop">PRODUCTS</a><a>ABOUT US</a><a>MISSION</a><a>REQUEST INFORMATION</a><a>CONTACTS</a>
    </nav>
  </header>

  <section class="slider">
    <svg class="bg" width="939" height="304" viewBox="0 0 939 304">
      <defs><linearGradient id="sb" x1="0" y1="0" x2="0" y2="1"><stop offset="0" stop-color="#4a87c9"/><stop offset="1" stop-color="#2f68ab"/></linearGradient></defs>
      <path d="M553 0 H939 V304 H256 L285 270 H440 C500 230 520 120 553 0 Z" fill="url(#sb)"/>
      <line x1="0" y1="270" x2="290" y2="270" stroke="#ccc"/>
    </svg>
    <div class="slide-photo" role="img" aria-label="Photo of a fiberglass axial duct fan"></div>
    <svg class="arrow prev" width="26" height="32"><path d="M24 2 L6 16 L24 30 L18 16 Z" fill="#7ea2c8"/></svg>
    <svg class="arrow next" width="26" height="32"><path d="M2 2 L20 16 L2 30 L8 16 Z" fill="#7ea2c8"/></svg>
    <p class="slide-copy">We have a wide selecion of fiberglass fans and other corrosion resistant air handling solutions for OEMs, Contractors and Plant Maintenance Operations.</p>
    <p class="slide-copy reflect" aria-hidden="true">solutions for OEMs, Contractors and Plant Maintenance Operations.</p>
    <div class="caption">Fiberglass axial fans</div>
    <div class="dots"><i class="on"></i><i></i><i></i><i></i><i></i></div>
  </section>

  <section class="selection">
    <h2>PRODUCT SELECTION</h2>
    <div class="field"></div>
    <div class="btn">Submit</div>
    <p>To verify a catalog numberand access product information, enter the complete number (including dashes) above.</p>
  </section>

  <section class="products">
    <div class="card"><div class="frame"></div><h3>Fiberglass Centrifugal Fans</h3><div class="photo" role="img" aria-label="Photo of a fiberglass centrifugal fan"></div><div class="more">more &gt;&gt;</div></div>
    <div class="card"><div class="frame"></div><h3>High Plume Exhaust Fans</h3><div class="photo" role="img" aria-label="Photo of high plume exhaust fans"></div><div class="more">more &gt;&gt;</div></div>
    <div class="card"><div class="frame"></div><h3>Fiberglass Louvers &amp; Dampers</h3><div class="photo" role="img" aria-label="Photo of a fiberglass damper"></div><div class="more">more &gt;&gt;</div></div>
    <div class="card"><div class="frame"></div><h3>Fiberglass axial Propellers</h3><div class="photo" role="img" aria-label="Photo of a fiberglass axial propeller"></div><div class="more">more &gt;&gt;</div></div>
    <div class="card"><div class="frame"></div><h3>Fiberglass Axial Fans</h3><div class="photo" role="img" aria-label="Photo of a fiberglass axial fan"></div><div class="more">more &gt;&gt;</div></div>
  </section>

  <footer class="footer">
    <h4 style="left:63px">TESTIMONIALS</h4>
    <div class="bubble">I have been very satisfied with all of the service provided by <b>DFC</b>. All of your personnel are really focused and were so courteous and professional acting.</div>
    <svg class="bubble-tail" width="50" height="26"><path d="M0 0 H40 L50 26 Z" fill="#1c1a1b"/></svg>
    <div class="author">Mr. Dalton</div>

    <h4 style="left:323px">FOLLOW US</h4>
    <div class="social" aria-label="Social links"><i></i><i></i><i></i><i></i><i></i><i></i><i></i></div>

    <h4 style="left:582px">NEWSLETTER</h4>
    <div class="form-box" style="left:511px">
      <div class="in" style="top:13px">Your Name</div>
      <div class="in" style="top:41px">Your Email</div>
      <div class="fbtn" style="left:163px;top:85px;width:53px;background:var(--red)">Submit</div>
    </div>

    <h4 style="left:870px">QUICK CONTACT</h4>
    <div class="form-box" style="left:805px">
      <div class="in" style="top:13px">Your Email</div>
      <div class="in" style="top:41px;height:39px">Your Message</div>
      <div class="fbtn" style="left:98px;top:85px;width:53px;background:var(--blue)">Reset</div>
      <div class="fbtn" style="left:159px;top:85px;width:53px;background:var(--red)">Submit</div>
    </div>
  </footer>
</div>
<div class="copyright">Copyright © &nbsp;DFC &nbsp;2013. All rights reserved.</div>
</body>
</html>
```